Criação de Papelaria (6 itens) para Logística, Entrega & Armazenamento
A empresa queria:
" Trabalhamos no seguinte de logística, no qual engloba diversos seguimentos, como armazenagem, transporte , manuseio e entregas. Nosso foco é o atendimento personalizado ao cliente, suprindo toda a demanda e necessidade do cliente sem ocasionar nenhum transtorno ao mesmo. "

```html
<!DOCTYPE html>
<html lang="pt-BR">
<head>
<meta charset="UTF-8">
<title>Pasta – Rumo Certo Soluções Logísticas</title>
<link href="https://fonts.googleapis.com/css2?family=Exo+2:wght@400;700;800&display=swap" rel="stylesheet">
<style>
  :root{
    --bg:#2b2b2d;
    --red:#c51f2b;
    --red-dark:#a5161f;
    --paper:#f4f4f4;
    --paper-shade:#dcdcdc;
    --ink:#6d6d6d;
    --white:#ffffff;
  }
  *{margin:0;padding:0;box-sizing:border-box}
  html,body{width:1200px;height:1200px;overflow:hidden}
  body{background:var(--bg);font-family:"Exo 2",Arial,sans-serif;display:flex;align-items:center;justify-content:center}
  .folder{display:flex;width:960px;height:680px;box-shadow:0 20px 50px rgba(0,0,0,.45)}
  .panel{position:relative;width:480px;height:680px;overflow:hidden}
  .panel--back{background:linear-gradient(90deg,var(--paper) 0%,var(--white) 60%,var(--paper-shade) 100%)}
  .panel--front{background:linear-gradient(100deg,var(--red-dark) 0%,var(--red) 25%,var(--red) 100%)}

  .brand{position:absolute;text-align:left}
  .brand__name{font-weight:800;font-size:46px;letter-spacing:3px;line-height:1;text-transform:uppercase}
  .brand__tag{font-weight:400;font-size:13.5px;letter-spacing:6.2px;text-transform:uppercase;margin-top:6px}
  .panel--back .brand{left:70px;top:280px}
  .panel--back .brand__name,.panel--back .brand__tag{color:var(--red)}
  .panel--front .brand{left:70px;top:60px}
  .panel--front .brand__name{font-size:36px}
  .panel--front .brand__tag{font-size:10.5px;letter-spacing:4.9px}
  .panel--front .brand__name,.panel--front .brand__tag{color:var(--white)}

  .contacts{position:absolute;left:40px;right:30px;bottom:40px;display:flex;justify-content:space-between;font-size:9.5px;color:var(--ink);line-height:1.9}
  .contacts__col{display:flex;flex-direction:column}
  .contacts__item{display:flex;align-items:center;gap:6px}
  .contacts__item svg{width:9px;height:9px;fill:var(--red)}

  .services{position:absolute;left:0;top:0;width:480px;height:680px}
</style>
</head>
<body>
  <main class="folder">
    <section class="panel panel--back">
      <div class="brand">
        <div class="brand__name">Rumo Certo</div>
        <div class="brand__tag">Soluções Logísticas</div>
      </div>
      <div class="contacts">
        <div class="contacts__col">
          <span class="contacts__item"><svg viewBox="0 0 10 10"><path d="M2 0h2l1 3-1.5 1a6 6 0 0 0 2.5 2.5L7 5l3 1v2c0 1-1 2-2 2A8 8 0 0 1 0 2c0-1 1-2 2-2z"/></svg>(19) 3251-7780</span>
          <span class="contacts__item"><svg viewBox="0 0 10 10"><path d="M2 0h2l1 3-1.5 1a6 6 0 0 0 2.5 2.5L7 5l3 1v2c0 1-1 2-2 2A8 8 0 0 1 0 2c0-1 1-2 2-2z"/></svg>(19) 99712-0395</span>
        </div>
        <div class="contacts__col">
          <span class="contacts__item">contato@rumocerto.com.br</span>
          <span class="contacts__item">www.rumocerto.com.br</span>
        </div>
        <div class="contacts__col">
          <span class="contacts__item"><svg viewBox="0 0 10 10"><path d="M5 0a3.5 3.5 0 0 1 3.5 3.5C8.5 6 5 10 5 10S1.5 6 1.5 3.5A3.5 3.5 0 0 1 5 0zm0 2a1.5 1.5 0 1 0 0 3 1.5 1.5 0 0 0 0-3z"/></svg>Rua das Acácias, 210 – Centro</span>
          <span class="contacts__item">Campinas/SP CEP 13000-000</span>
        </div>
      </div>
    </section>

    <section class="panel panel--front">
      <div class="brand">
        <div class="brand__name">Rumo Certo</div>
        <div class="brand__tag">Soluções Logísticas</div>
      </div>
      <svg class="services" viewBox="0 0 480 680" role="img" aria-label="Ícones de serviços: armazenagem, transporte, localização, entrega">
        <g fill="none" stroke="#ffffff" stroke-width="2">
          <circle cx="120" cy="400" r="14"/>
          <circle cx="128" cy="350" r="14"/>
          <circle cx="150" cy="305" r="14"/>
          <circle cx="185" cy="270" r="14"/>
          <circle cx="230" cy="248" r="14"/>
          <circle cx="280" cy="240" r="14"/>
          <circle cx="330" cy="246" r="14"/>
        </g>
        <g fill="#ffffff">
          <rect x="114" y="394" width="12" height="12"/>
          <path d="M128 343v14M121 350h14" stroke="#fff" stroke-width="2.5"/>
          <path d="M150 297a5 5 0 0 1 5 5c0 4-5 10-5 10s-5-6-5-10a5 5 0 0 1 5-5z"/>
          <path d="M178 270l5 5 9-10" fill="none" stroke="#fff" stroke-width="2.5"/>
          <path d="M222 248h12l-4-4M234 248l-4 4" fill="none" stroke="#fff" stroke-width="2.5"/>
          <path d="M276 234h2l1 3-1.5 1a6 6 0 0 0 2.5 2.5l1-1.5 3 1v2c0 1-1 2-2 2a8 8 0 0 1-8-8c0-1 1-2 2-2z"/>
          <rect x="323" y="241" width="14" height="10" rx="1"/>
        </g>
      </svg>
    </section>
  </main>
</body>
</html>
```